body balm label design

body balm tube design, current label design for other similar products
Need to have a design which can interchange between 3 different solutions
Quiet Orchard (Lavender + Vanilla)
Copper Trail (Eucalyptus + Mint)
Fern Hollow (Bergamot + Cedarwood)
Tube size:
2.5h x 3.25 w
Target Market(s)
natural, solution focused
Requirements
Must have
- relatable to existing brand designs, focus on features and benefits

```html
<!DOCTYPE html>
<html lang="en">
<head>
<meta charset="utf-8">
<title>Body Balm Aromatherapy Labels</title>
<link rel="stylesheet" href="https://fonts.googleapis.com/css2?family=Montserrat:wght@400&family=Open+Sans:ital,wght@1,400&family=Saira+Semi+Condensed:wght@400&display=swap">
<style>
  :root {
    --canvas: #efefed;
    --canvas-art: #f4f4f2;
    --paper: #ffffff;
    --lavender: #9b9cc6;
    --sage: #7b9b89;
    --olive: #857c5b;
    --white: #ffffff;
  }
  * { margin: 0; padding: 0; box-sizing: border-box; }
  html, body {
    width: 800px;
    height: 1200px;
    overflow: hidden;
    background: var(--canvas);
  }
  .canvas {
    position: relative;
    width: 800px;
    height: 1200px;
    background: var(--canvas);
  }
  .backdrop-art {
    position: absolute;
    inset: 0;
    background: radial-gradient(circle at 20% 25%, var(--canvas-art), transparent 40%),
                radial-gradient(circle at 80% 55%, var(--canvas-art), transparent 40%),
                radial-gradient(circle at 15% 85%, var(--canvas-art), transparent 35%),
                var(--canvas);
  }
  .label {
    position: absolute;
    left: 272px;
    width: 256px;
    height: 334px;
    background: var(--paper);
    display: flex;
  }
  .label--sleep { top: 50px; --tone: var(--lavender); }
  .label--relief { top: 434px; --tone: var(--sage); }
  .label--calm { top: 817px; --tone: var(--olive); }

  .band {
    position: relative;
    flex: 0 0 74px;
    width: 74px;
    height: 334px;
    background: var(--tone);
    overflow: hidden;
  }
  .band-inner {
    position: absolute;
    left: 0;
    top: 334px;
    width: 334px;
    height: 74px;
    transform-origin: 0 0;
    transform: rotate(-90deg);
    padding: 10px 14px 0 16px;
    color: var(--white);
  }
  .product-name {
    font-family: "Saira Semi Condensed", "Arial Narrow", sans-serif;
    font-weight: 400;
    font-size: 29px;
    line-height: 40px;
    letter-spacing: 2px;
    text-transform: uppercase;
    white-space: nowrap;
  }
  .claims {
    font-family: "Open Sans", sans-serif;
    font-style: italic;
    font-size: 10px;
    line-height: 14px;
    padding-left: 52px;
    white-space: nowrap;
    opacity: 0.95;
  }

  .panel {
    position: relative;
    flex: 1;
    min-width: 0;
    text-align: center;
    color: var(--tone);
  }
  .title {
    position: absolute;
    top: 24px;
    left: 0;
    right: 0;
    font-family: "Montserrat", sans-serif;
    font-weight: 400;
    font-size: 17px;
    letter-spacing: 5px;
    padding-left: 5px;
  }
  .subtitle {
    position: absolute;
    top: 45px;
    left: 0;
    right: 0;
    font-family: "Open Sans", sans-serif;
    font-style: italic;
    font-size: 14px;
    letter-spacing: 1px;
  }
  .botanical {
    position: absolute;
    left: 28px;
    top: 96px;
    width: 128px;
    height: 128px;
  }
  .ingredients {
    position: absolute;
    top: 273px;
    left: 4px;
    right: 4px;
    font-family: "Saira Semi Condensed", "Arial Narrow", sans-serif;
    font-weight: 400;
    font-size: 15px;
    letter-spacing: 0.3px;
    white-space: nowrap;
  }
  .badge {
    position: absolute;
    left: 48px;
    bottom: 0;
    width: 86px;
    height: 23px;
    background: var(--tone);
    border-radius: 6px 6px 0 0;
    color: var(--white);
    font-family: "Montserrat", sans-serif;
    font-size: 7.5px;
    line-height: 23px;
    letter-spacing: 0.3px;
  }
</style>
</head>
<body>
<main class="canvas">
  <div class="backdrop-art" role="img" aria-label="Faint white line engravings of vanilla orchid, mint leaves and citrus slices across the background"></div>

  <section class="label label--sleep">
    <div class="band">
      <div class="band-inner">
        <p class="product-name">Quiet Orchard</p>
        <p class="claims">plant based &nbsp;·&nbsp; vegan &nbsp;·&nbsp; cruelty free</p>
      </div>
    </div>
    <div class="panel">
      <h2 class="title">BODY BALM</h2>
      <p class="subtitle">Aromatherapy</p>
      <svg class="botanical" viewBox="0 0 128 128" role="img" aria-label="Engraved illustration of lavender sprigs and a vanilla orchid over a lavender circle">
        <circle cx="64" cy="64" r="62" fill="var(--lavender)"/>
      </svg>
      <p class="ingredients">Lavender + Vanilla</p>
      <p class="badge">100% NATURAL</p>
    </div>
  </section>

  <section class="label label--relief">
    <div class="band">
      <div class="band-inner">
        <p class="product-name">Copper Trail</p>
        <p class="claims">plant based &nbsp;·&nbsp; vegan &nbsp;·&nbsp; cruelty free</p>
      </div>
    </div>
    <div class="panel">
      <h2 class="title">BODY BALM</h2>
      <p class="subtitle">Aromatherapy</p>
      <svg class="botanical" viewBox="0 0 128 128" role="img" aria-label="Engraved illustration of eucalyptus branch and mint leaves over a sage circle">
        <circle cx="64" cy="64" r="62" fill="var(--sage)"/>
      </svg>
      <p class="ingredients">Eucalyptus + Mint</p>
      <p class="badge">100% NATURAL</p>
    </div>
  </section>

  <section class="label label--calm">
    <div class="band">
      <div class="band-inner">
        <p class="product-name">Fern Hollow</p>
        <p class="claims">plant based &nbsp;·&nbsp; vegan &nbsp;·&nbsp; cruelty free</p>
      </div>
    </div>
    <div class="panel">
      <h2 class="title">BODY BALM</h2>
      <p class="subtitle">Aromatherapy</p>
      <svg class="botanical" viewBox="0 0 128 128" role="img" aria-label="Engraved illustration of bergamot fruit, cedarwood log and leaves over an olive circle">
        <circle cx="64" cy="64" r="62" fill="var(--olive)"/>
      </svg>
      <p class="ingredients">Bergamot + Cedarwood</p>
      <p class="badge">100% NATURAL</p>
    </div>
  </section>
</main>
</body>
</html>
```